Vintrel.com- International Goal Achievement Coach Needs Website Design

I need a web design for my new company called Vintrel. I help people who are stuck, people who have a big dream, but don't know how to get there. I help them to break their dreams down into small, manageable steps... and then I'm the "kick in the shin" to get them moving and thriving!

We can all be better- We can all DO better. I inspire people to Ride Onward in the direction of your dreams.

I have uploaded my logo along with some vintage champagne posters. Please use the vintage posters as inspiration. I like the bold, vintage look and feel. I would love the main colors of the design to be black, white and metallic gold. And to follow along this vintage look and feel. Please feel free to use the logo in black or metallic gold or white.

Target Market(s)

websites that I like- janetrulsby.com & hollyp.tv

I would like to also use the vintage champagne photos attached as inspiration as well.

Industry/Entity Type

It Company

Requirements
Must have
• Tabs should include: About, Work With Me, Praise, Giving Back

On the homepage add:
* Sign up for newsletter with space to enter name and email (No click throughs)
* Upcoming Events/Sessions
* Newsletter Posts
* Resources
* Praise Section

* Large photo on top with additional photos throughout the page/site.
Nice to have
• Any additions you can bring to the table would be greatly appreciated.

```html
<!DOCTYPE html>
<html lang="en">
<head>
<meta charset="utf-8">
<title>Vintrel</title>
<link href="https://fonts.googleapis.com/css2?family=Merriweather:wght@700;900&family=Open+Sans:wght@400;600;700&display=swap" rel="stylesheet">
<style>
:root{
  --bronze:#a57a52;
  --bronze-dark:#8e6640;
  --olive:#c8c58c;
  --olive-text:#7d7640;
  --ink:#2a2a2a;
  --body:#4a4a4a;
  --muted:#8a8a8a;
  --rule:#e2e2e2;
  --panel:#efeeea;
  --white:#ffffff;
  --field:#f1f1f1;
}
*{box-sizing:border-box;margin:0;padding:0}
html,body{width:1200px;height:2866px;overflow:hidden}
body{position:relative;background:var(--white);font-family:"Open Sans",Arial,sans-serif;color:var(--body)}
.abs{position:absolute}

/* header */
.brand{left:130px;top:27px;display:flex;align-items:center;gap:14px}
.brand-mark{width:62px;height:62px;border-radius:50%;background:var(--bronze)}
.brand-name{font-family:"Open Sans",Arial,sans-serif;font-weight:600;font-size:30px;color:var(--bronze)}
.search{left:848px;top:46px;width:220px;height:34px;background:var(--field)}
.search svg{position:absolute;right:10px;top:9px}

/* hero */
.hero{left:0;top:115px;width:1200px;height:428px;background:linear-gradient(90deg,#3f5560 0%,#55707a 35%,#4a6570 60%,#3b4f58 100%)}
.hero-person{left:707px;top:115px;width:250px;height:428px;background:linear-gradient(180deg,#5e7fa0 0%,#4b6f93 60%,#b29272 100%);border-radius:110px 110px 0 0}
.hero-title{left:132px;top:188px;width:540px;font-family:"Merriweather",Georgia,serif;font-weight:900;font-size:33px;line-height:46px;color:var(--white);letter-spacing:.5px}
.hero-sub{left:135px;top:350px;font-size:16px;line-height:31px;color:var(--white)}
.field{top:436px;height:38px;width:198px;background:var(--white);font-size:12px;color:#777;padding:11px 16px}
.yes{left:563px;top:422px;width:70px;height:70px;border-radius:50%;background:var(--olive);color:#4a4630;font-size:12px;line-height:16px;text-align:center;padding-top:19px}
.hero-next{left:1049px;top:327px}

/* nav */
.nav{left:0;top:543px;width:1200px;height:51px;background:var(--bronze)}
.nav a{position:absolute;top:0;height:51px;line-height:51px;color:var(--white);font-size:13px;text-decoration:none;transform:translateX(-50%)}
.nav .active{left:176px;width:92px;text-align:center;background:var(--bronze-dark)}

/* posts */
.post{left:130px;width:606px;height:644px}
.post-title{position:absolute;top:0;left:0;font-size:28px;line-height:38px;font-weight:600;color:var(--ink);letter-spacing:.4px}
.comments{position:absolute;top:85px;left:0;width:128px;height:34px;background:var(--bronze);color:var(--white);font-size:13px;font-weight:700;text-align:center;line-height:34px}
.post-photo{position:absolute;top:140px;left:0;width:606px;height:306px}
.post-text{position:absolute;top:466px;left:0;width:606px;font-size:13.4px;line-height:26px;color:var(--body)}
.post-foot{position:absolute;top:591px;left:0;width:606px;height:53px;border-top:1px solid var(--rule);border-bottom:1px solid var(--rule)}
.more{position:absolute;left:6px;top:16px;font-size:13px;color:var(--bronze)}
.share{position:absolute;right:0;top:14px;display:flex;gap:10px;align-items:center}
.chip{display:flex;align-items:center;gap:3px}
.chip b{font-size:11px;font-weight:700;color:#555;border:1px solid #c9c9c9;border-radius:3px;padding:1px 6px;background:#f6f6f6}
.chip i{font-style:normal;font-size:10px;color:#666;border:1px solid #d6d6d6;border-radius:3px;padding:1px 5px}

/* sidebar */
.events{left:770px;top:659px;width:300px;height:396px;background:var(--olive)}
.side-h{font-size:22px;color:var(--ink)}
.events .side-h{position:absolute;left:20px;top:24px}
.events-photo{position:absolute;left:15px;top:63px;width:270px;height:159px;border:4px solid var(--white);background:linear-gradient(135deg,#c9c9c9,#7a7a7a)}
.events-date{position:absolute;left:16px;top:243px;font-size:16px;color:var(--olive-text)}
.events-text{position:absolute;left:16px;top:270px;width:270px;font-size:13px;line-height:25px;color:#3a3827}
.events-more{position:absolute;left:16px;top:350px;font-size:13px;color:var(--white)}
.quote{left:770px;top:1095px;width:300px;height:204px;background:var(--panel)}
.quote-text{position:absolute;left:26px;top:24px;width:260px;font-size:13px;line-height:25px;color:#444}
.quote-by{position:absolute;right:30px;top:126px;font-size:13px;color:var(--bronze)}
.quote-next{position:absolute;left:26px;top:152px;font-size:13px;color:var(--muted)}
.quote-tip{left:900px;top:1299px}
.side-photo{left:770px;top:1345px;width:300px;height:161px;background:linear-gradient(90deg,#5b4a3a,#6e7f95 50%,#5a4838)}
.popular-h{left:770px;top:1548px;width:300px;padding-bottom:8px;border-bottom:1px solid var(--rule)}
.pop{left:770px;width:280px;font-size:13px;line-height:26px;color:var(--bronze)}
.find{left:770px;top:1930px;width:300px;padding-bottom:10px;border-bottom:1px solid var(--rule);font-size:13px;color:var(--ink)}
.find span{color:var(--bronze)}
.awards-h{left:770px;top:2002px}
.awards{left:770px;top:2041px;width:300px;height:119px;background:var(--panel)}
.badge{position:absolute;top:16px;width:88px;height:88px;border-radius:50%;background:#3b3b3b}

/* footer */
.footer{left:0;top:2752px;width:1200px;height:114px;background:var(--olive)}
.foot-nav{position:absolute;top:34px;left:0;width:1200px;display:flex;justify-content:center;gap:34px;font-size:13px;color:var(--ink)}
.foot-legal{position:absolute;top:66px;left:0;width:1200px;text-align:center;font-size:12px;color:var(--ink)}
</style>
</head>
<body>

<header>
  <div class="abs brand"><span class="brand-mark"></span><span class="brand-name">Vintrel</span></div>
  <div class="abs search">
    <svg width="16" height="16" viewBox="0 0 16 16"><circle cx="6.5" cy="6.5" r="4.5" fill="none" stroke="#555" stroke-width="1.8"/><line x1="10" y1="10" x2="14" y2="14" stroke="#555" stroke-width="2"/></svg>
  </div>
</header>

<section>
  <div class="abs hero" role="img" aria-label="Weathered blue wooden barn door background"></div>
  <div class="abs hero-person" role="img" aria-label="Smiling coach in sunglasses and denim jacket"></div>
  <h1 class="abs hero-title">I'M THE "KICK IN THE SHIN" TO GET THEM MOVING AND THRIVING!</h1>
  <p class="abs hero-sub">I help people who are stuck, people who have a big dream,<br>but don't know how to get there.</p>
  <div class="abs field" style="left:132px">First Name</div>
  <div class="abs field" style="left:346px">Email</div>
  <div class="abs yes">Yes<br>Please</div>
  <svg class="abs hero-next" width="38" height="38" viewBox="0 0 38 38"><circle cx="19" cy="19" r="17" fill="rgba(0,0,0,.25)" stroke="#fff" stroke-width="2"/><path d="M15 11 L24 19 L15 27" fill="none" stroke="#fff" stroke-width="3"/></svg>
</section>

<nav class="abs nav">
  <a class="active" style="left:176px">HOME</a>
  <a style="left:287px">ABOUT US</a>
  <a style="left:403px">BOOKS</a>
  <a style="left:506px">EVENTS</a>
  <a style="left:604px">PRESS</a>
  <a style="left:715px">CONTACT</a>
  <a style="left:812px">FUTURE</a>
</nav>

<main>
  <article class="abs post" style="top:655px">
    <h2 class="post-title">APEIRIAN DEMOCRITUM EINAM, DOMING<br>NEGLEGENTUR AD VIS</h2>
    <div class="comments">56 Comment</div>
    <div class="post-photo" role="img" aria-label="Young man reading a book seated in autumn leaves" style="background:linear-gradient(135deg,#d9a847,#c8832a 50%,#e6c06a)"></div>
    <p class="post-text">Ea eam labores imperdiet, apeirian democritum ei nam, doming neglegentur ad vis. Ne malorum ceteros feugait quo, ius ea liber offendit placerat, est habemus aliquyam legendos id. Eam no corpora maluisset definitiones, eam mucius malorum id. Quo ea idque commodo utroque, per ex eros etiam accumsan. Ea eam labores imperdiet, apeirian democritum.</p>
    <div class="post-foot">
      <span class="more">Continue Reading &nbsp;⟶</span>
      <div class="share"><span class="chip"><b>Like</b><i>1.5k</i></span><span class="chip"><b>Share</b><i>232</i></span><span class="chip"><b>+1</b><i>15</i></span><span class="chip"><b>Save</b><i>5</i></span></div>
    </div>
  </article>

  <article class="abs post" style="top:1358px">
    <h2 class="post-title">APEIRIAN DEMOCRITUM EINAM, DOMING<br>NEGLEGENTUR AD VIS</h2>
    <div class="comments">56 Comment</div>
    <div class="post-photo" role="img" aria-label="Two young men in caps and overalls leaning on a brick wall" style="background:linear-gradient(90deg,#6f6f6a,#9a9a92 50%,#8b8b85)"></div>
    <p class="post-text">Ea eam labores imperdiet, apeirian democritum ei nam, doming neglegentur ad vis. Ne malorum ceteros feugait quo, ius ea liber offendit placerat, est habemus aliquyam legendos id. Eam no corpora maluisset definitiones, eam mucius malorum id. Quo ea idque commodo utroque, per ex eros etiam accumsan. Ea eam labores imperdiet, apeirian democritum.</p>
    <div class="post-foot">
      <span class="more">Continue Reading &nbsp;⟶</span>
      <div class="share"><span class="chip"><b>Like</b><i>1.5k</i></span><span class="chip"><b>Share</b><i>232</i></span><span class="chip"><b>+1</b><i>15</i></span><span class="chip"><b>Save</b><i>5</i></span></div>
    </div>
  </article>

  <article class="abs post" style="top:2054px">
    <h2 class="post-title">APEIRIAN DEMOCRITUM EINAM, DOMING<br>NEGLEGENTUR AD VIS</h2>
    <div class="comments">56 Comment</div>
    <div class="post-photo" role="img" aria-label="Sepia portrait of the coach in a denim jacket by a wooden door" style="background:linear-gradient(90deg,#4a4236,#8a7f6c 50%,#5a5043)"></div>
    <p class="post-text">Ea eam labores imperdiet, apeirian democritum ei nam, doming neglegentur ad vis. Ne malorum ceteros feugait quo, ius ea liber offendit placerat, est habemus aliquyam legendos id. Eam no corpora maluisset definitiones, eam mucius malorum id. Quo ea idque commodo utroque, per ex eros etiam accumsan. Ea eam labores imperdiet, apeirian democritum.</p>
    <div class="post-foot">
      <span class="more">Continue Reading &nbsp;⟶</span>
      <div class="share"><span class="chip"><b>Like</b><i>1.5k</i></span><span class="chip"><b>Share</b><i>232</i></span><span class="chip"><b>+1</b><i>15</i></span><span class="chip"><b>Save</b><i>5</i></span></div>
    </div>
  </article>
</main>

<aside>
  <div class="abs events">
    <h3 class="side-h">Hot Events</h3>
    <div class="events-photo" role="img" aria-label="Black and white portrait of a young man in glasses"></div>
    <div class="events-date">October 12, 2014</div>
    <p class="events-text">Eu mei solum oporteat eleifend, libris nominavi maiestatis duo at, quod dissentiet vel te. Legere prompta impedit id eum.</p>
    <div class="events-more">Continue Reading &nbsp;⟶</div>
  </div>

  <div class="abs quote">
    <p class="quote-text">"Ea eam labores imperdiet, apeirian democritum ei nam, doming neglegentur ad vis. Ne malorum ceteros feugait quo, ius ea liber offendit placerat."</p>
    <div class="quote-by">- Dana Whitlow</div>
    <div class="quote-next">Next Qoute &nbsp;⟶</div>
  </div>
  <svg class="abs quote-tip" width="36" height="19" viewBox="0 0 36 19"><path d="M0 0 H36 L18 19 Z" fill="#efeeea"/></svg>

  <div class="abs side-photo" role="img" aria-label="Coach in sunglasses leaning against a wooden doorway"></div>

  <h3 class="abs side-h popular-h">Most Popular</h3>
  <p class="abs pop" style="top:1602px">Ne malorum ceteros feugait quo, ius ea liber offendit placerat, est habemus</p>
  <p class="abs pop" style="top:1678px">Aliquyam legendos id. Eam no corpora maluisset definitiones, eam mucius malorum id.</p>
  <p class="abs pop" style="top:1757px">Quo ea idque commodo utroque, per ex eros etiam accumsan. Ea eam labores imperdiet, apeirian democritum.</p>
  <p class="abs pop" style="top:1858px">Ne malorum ceteros feugait quo, ius ea liber offendit placerat, est habemus</p>
  <p class="abs find">Find more posts in our <span>Archives &gt;&gt;</span></p>

  <h3 class="abs side-h awards-h">Awards</h3>
  <div class="abs awards">
    <span class="badge" style="left:36px"></span>
    <span class="badge" style="left:176px"></span>
  </div>
</aside>

<footer class="abs footer">
  <div class="foot-nav"><span>ABOUT</span><span>WORK WITH ME</span><span>PRAISE</span><span>GIVING BACK</span><span>RESOURCES</span><span>ARCHIVES</span><span>CONTACT</span></div>
  <div class="foot-legal">PRIVACY POLICY &nbsp;| &nbsp;© 2014 Your Sitel. &nbsp;| &nbsp;TERMS POLICY &nbsp;| &nbsp;DISCLAIMER</div>
</footer>

</body>
</html>
```